Update Law Firm Website

Update law firm website pages, add pages for employees. Current website looks stale. www.vantholmlegal.example

Target Market(s)

Personal injury clients

Industry/Entity Type

Legal

Number of Pages Required

5+ page

Font styles to use
Serif

Requirements
Must have
• User friendly and engaging design
Nice to have
• ?
Should not have
• scales of justice, law books,

```html
<!DOCTYPE html>
<html lang="en">
<head>
<meta charset="utf-8">
<title>Vantholm Injury Law Group</title>
<link href="https://fonts.googleapis.com/css2?family=Montserrat:wght@400;500;600;700&family=Open+Sans:wght@400;600;700&display=swap" rel="stylesheet">
<style>
:root{
  --maroon:#7a0e14;
  --maroon-dark:#5c0a0e;
  --red:#9b2a2e;
  --gold:#b8891e;
  --gold-band:#a67a14;
  --yellow:#fdd06b;
  --grey-band:#e8e8e8;
  --ink:#222;
  --text:#444;
  --white:#fff;
}
*{margin:0;padding:0;box-sizing:border-box}
html,body{width:1200px;height:2791px;overflow:hidden}
body{position:relative;background:var(--white);font-family:"Open Sans",sans-serif;color:var(--text)}
.abs{position:absolute}

/* header */
.brand-mark{left:99px;top:34px;width:40px;height:40px;border-radius:50%;background:var(--maroon)}
.brand-name{left:152px;top:28px;font-family:"Montserrat",sans-serif;font-weight:700;font-size:21px;line-height:26px;color:var(--maroon)}
.contact-chip{top:36px;height:36px;display:flex;align-items:center;gap:12px;font-size:15px;font-weight:600;color:var(--ink);white-space:nowrap}
.chip-icon{width:36px;height:36px;border-radius:50%;display:flex;align-items:center;justify-content:center;flex:none}
.social-sq{top:44px;width:20px;height:20px;background:#8a8a8a}

/* nav */
.main-nav{left:0;top:112px;width:1200px;height:52px;background:var(--maroon)}
.nav-item{top:17px;font-family:"Montserrat",sans-serif;font-weight:600;font-size:15px;color:var(--white);white-space:nowrap}

/* hero */
.hero-photo{left:0;top:172px;width:1200px;height:514px;background:linear-gradient(100deg,#d8d2c8 0%,#c9c2b6 35%,#a9a3a0 60%,#5d5a5e 100%)}
.hero-title{left:99px;top:280px;font-family:"Montserrat",sans-serif;font-weight:600;font-size:36px;line-height:48px;color:var(--white);text-shadow:0 2px 4px rgba(0,0,0,.35)}
.hero-sub{left:99px;top:398px;font-size:18px;line-height:34px;color:var(--white);text-shadow:0 1px 3px rgba(0,0,0,.4)}
.btn{display:flex;align-items:center;justify-content:center;color:var(--white);font-weight:600;font-family:"Montserrat",sans-serif}
.hero-btn{left:99px;top:485px;width:119px;height:45px;background:#8a2a2a;font-size:14px}
.hero-arrow{top:410px}

/* intro */
.section-title{font-family:"Montserrat",sans-serif;font-weight:600;color:var(--maroon)}
.intro-title{left:99px;top:733px;font-size:26px}
.intro-rule{left:99px;top:772px;width:440px;height:2px;background:var(--maroon)}
.intro-sub{left:99px;top:797px;font-family:"Montserrat",sans-serif;font-weight:600;font-size:18px;color:var(--ink)}
.portrait{left:99px;top:841px;width:109px;height:119px;background:linear-gradient(160deg,#7d6a5c,#2c2a30)}
.intro-text{font-size:12.5px;line-height:23px;color:var(--text);text-align:justify}
.intro-btn{left:99px;top:1043px;width:115px;height:43px;background:var(--maroon-dark);font-size:14px}

.consult{left:788px;top:746px;width:313px;height:337px;border:4px solid #f1ede4;background:var(--yellow);box-shadow:0 14px 12px -10px rgba(0,0,0,.25)}
.consult-title{left:0;top:34px;width:305px;text-align:center;font-weight:700;font-size:17px;color:var(--white)}
.field{background:var(--white);font-size:11px;color:#555;padding-left:8px;display:flex;align-items:center}
.consult .field{left:15px;width:276px;height:32px}
.submit-btn{left:15px;top:247px;width:276px;height:42px;background:linear-gradient(#8e1d23,var(--maroon-dark));font-size:15px;font-family:"Open Sans",sans-serif;font-weight:700;border-radius:3px}

/* cases */
.cases{left:0;top:1137px;width:1200px;height:453px;background:var(--gold-band)}
.cases-title{left:0;top:1176px;width:1200px;text-align:center;font-family:"Montserrat",sans-serif;font-weight:600;font-size:25px;color:var(--white)}
.cases-rule{left:521px;top:1226px;width:158px;height:2px;background:var(--white)}
.case-icon{width:66px;height:50px;border:3px solid var(--white);border-radius:10px}
.case-title{font-weight:600;font-size:21px;color:var(--white)}
.case-text{width:335px;font-size:12px;line-height:22px;color:#f6ead0}

/* damages */
.damages{left:0;top:1590px;width:1200px;height:332px;background:var(--grey-band)}
.damage-label{width:170px;text-align:center;font-size:17px;line-height:28px;color:var(--ink)}

/* testimonials */
.testi-photo{width:138px;height:138px;border-radius:50%;border:3px solid var(--maroon);padding:6px}
.testi-photo span{display:block;width:100%;height:100%;border-radius:50%;background:linear-gradient(160deg,#c8c3bf,#6b6560)}
.quote-mark{font-family:"Montserrat",sans-serif;font-weight:700;font-size:44px;line-height:1;color:var(--maroon)}
.testi-name{font-size:18px;color:var(--ink)}
.testi-role{font-size:13px;color:var(--maroon)}
.testi-text{width:480px;font-size:12px;line-height:22px;color:var(--text)}

/* footer */
.footer{left:0;top:2307px;width:1200px;height:484px;background:var(--red)}
.footer-title{left:99px;top:2357px;font-family:"Montserrat",sans-serif;font-weight:500;font-size:28px;color:var(--white)}
.footer-rule{left:99px;top:2403px;width:106px;height:2px;background:var(--white)}
.f-icon{width:48px;height:48px;border-radius:50%;background:var(--white);display:flex;align-items:center;justify-content:center}
.f-text{font-size:15px;line-height:30px;color:var(--white)}
.f-lead{left:484px;top:2360px;font-size:20px;color:var(--white);font-weight:600;white-space:nowrap}
.f-field{background:transparent;border:1.5px solid #e8c1c1;color:var(--white);font-size:13px;padding-left:8px;display:flex;align-items:center}
.send-btn{left:484px;top:2626px;width:117px;height:38px;background:var(--yellow);color:var(--maroon);font-size:14px;border:1px solid #c89b3c}
.footer-divider{left:99px;top:2701px;width:1000px;height:1px;background:#c97a7d}
.copyright{left:99px;top:2733px;font-size:13px;font-weight:600;color:var(--white)}
.f-social{top:2725px;width:34px;height:34px;border-radius:50%;border:1.5px solid var(--white)}
</style>
</head>
<body>

<header>
  <div class="abs brand-mark"></div>
  <div class="abs brand-name">VANTHOLM INJURY<br>LAW GROUP</div>

  <div class="abs contact-chip" style="left:468px">
    <span class="chip-icon" style="background:var(--maroon)">
      <svg width="16" height="12" viewBox="0 0 16 12"><rect x="0.5" y="0.5" width="15" height="11" fill="none" stroke="#fff"/><path d="M1 1l7 6 7-6" fill="none" stroke="#fff"/></svg>
    </span>info@vantholmlegal.example
  </div>
  <div class="abs contact-chip" style="left:776px;font-size:16px">
    <span class="chip-icon" style="background:#444">
      <svg width="16" height="16" viewBox="0 0 24 24"><path d="M6.6 10.8a15.1 15.1 0 006.6 6.6l2.2-2.2a1 1 0 011-.25 11.4 11.4 0 003.6.6 1 1 0 011 1V20a1 1 0 01-1 1A17 17 0 013 4a1 1 0 011-1h3.5a1 1 0 011 1 11.4 11.4 0 00.6 3.6 1 1 0 01-.25 1z" fill="#fff"/></svg>
    </span>(555) 014-2290
  </div>
  <div class="abs social-sq" style="left:962px"></div>
  <div class="abs social-sq" style="left:990px"></div>
  <div class="abs social-sq" style="left:1018px"></div>
  <div class="abs social-sq" style="left:1046px"></div>
  <div class="abs social-sq" style="left:1074px"></div>
</header>

<nav class="abs main-nav">
  <span class="abs nav-item" style="left:99px">Home</span>
  <span class="abs nav-item" style="left:182px">Slip and Fall</span>
  <span class="abs nav-item" style="left:314px">Auto Accident</span>
  <span class="abs nav-item" style="left:463px">Construction Injuries</span>
  <span class="abs nav-item" style="left:662px">Medical Malpractice</span>
  <span class="abs nav-item" style="left:854px">Results</span>
  <span class="abs nav-item" style="left:952px">About</span>
  <span class="abs nav-item" style="left:1042px">Contact</span>
</nav>

<section>
  <div class="abs hero-photo" role="img" aria-label="Photo of an injured older client in a neck brace reviewing documents with a lawyer"></div>
  <h1 class="abs hero-title">VANTHOLM INJURY<br>LAW GROUP</h1>
  <p class="abs hero-sub">Affordable and Essential Legal Advocate for<br>Your Injury Claim</p>
  <div class="abs btn hero-btn">READ MORE</div>
  <svg class="abs hero-arrow" style="left:28px" width="24" height="44" viewBox="0 0 24 44"><path d="M22 2L3 22l19 20" fill="none" stroke="#fff" stroke-width="2.5"/></svg>
  <svg class="abs hero-arrow" style="left:1136px" width="24" height="44" viewBox="0 0 24 44"><path d="M2 2l19 20L2 42" fill="none" stroke="#fff" stroke-width="2.5"/></svg>
</section>

<section>
  <h2 class="abs section-title intro-title">VANTHOLM INJURY LAW GROUP</h2>
  <div class="abs intro-rule"></div>
  <h3 class="abs intro-sub">Affordable and Essential Legal Advocate for Your Injury Claim</h3>
  <div class="abs portrait" role="img" aria-label="Portrait of attorney Marcus Hale"></div>
  <p class="abs intro-text" style="left:227px;top:838px;width:538px">When you are hit by a fatigued driver of a tractor-trailer or you suffer a fatal stroke because of a delayed diagnosis by a physician, the consequences can include staggering medical bills, debilitating pain and permanent disability. While overcoming the emotional, physical and financial hardships associated with a serious injury always present serious challenges, incidents resulting in substantial injuries can be even more traumatic.</p>
  <p class="abs intro-text" style="left:99px;top:979px;width:666px">Harbor City personal injury lawyer Marcus Hale recognizes that victims of distracted drivers, inattentive property owners and substandard medical providers might not focus on financial compensation.</p>
  <div class="abs btn intro-btn">Read More</div>

  <form class="abs consult">
    <div class="abs consult-title">FREE CONSULTATION FORM</div>
    <div class="abs field" style="top:68px">Name</div>
    <div class="abs field" style="top:110px">Phone</div>
    <div class="abs field" style="top:152px">Email</div>
    <div class="abs field" style="top:195px">Case</div>
    <div class="abs btn submit-btn">SUBMIT</div>
  </form>
</section>

<section>
  <div class="abs cases" role="img" aria-label="Gold-toned photo of a team of professionals in a meeting"></div>
  <h2 class="abs cases-title">PERSONAL INJURY CASES</h2>
  <div class="abs cases-rule"></div>

  <div class="abs case-icon" style="left:121px;top:1300px"></div>
  <h3 class="abs case-title" style="left:223px;top:1290px">Tractor-trailer Collisions</h3>
  <p class="abs case-text" style="left:223px;top:1327px">The firm is active in local civic and cultural affairs, and continues the tradition of providing quality legal services and diligent representation to clients throughout Logan.</p>

  <div class="abs case-icon" style="left:655px;top:1300px"></div>
  <h3 class="abs case-title" style="left:753px;top:1290px">Construction Accidents</h3>
  <p class="abs case-text" style="left:753px;top:1327px">The firm is active in local civic and cultural affairs, and continues the tradition of providing quality legal services and diligent representation to clients throughout Logan.</p>

  <div class="abs case-icon" style="left:121px;top:1437px"></div>
  <h3 class="abs case-title" style="left:223px;top:1427px">Motorcycle Crashes</h3>
  <p class="abs case-text" style="left:223px;top:1464px">The firm is active in local civic and cultural affairs, and continues the tradition of providing quality legal services and diligent representation to clients throughout Logan.</p>

  <div class="abs case-icon" style="left:655px;top:1437px"></div>
  <h3 class="abs case-title" style="left:753px;top:1427px">Medical Malpractice</h3>
  <p class="abs case-text" style="left:753px;top:1464px">The firm is active in local civic and cultural affairs, and continues the tradition of providing quality legal services and diligent representation to clients throughout Logan.</p>
</section>

<section>
  <div class="abs damages"></div>
  <h2 class="abs section-title" style="left:0;top:1638px;width:1200px;text-align:center;font-size:25px">TYPES OF DAMAGES</h2>
  <div class="abs" style="left:540px;top:1687px;width:120px;height:2px;background:var(--maroon)"></div>
  <svg class="abs" style="left:0;top:1730px" width="1200" height="84" viewBox="0 0 1200 84">
    <defs>
      <linearGradient id="damage-line" x1="167" x2="1032" gradientUnits="userSpaceOnUse">
        <stop offset="0" stop-color="#e0585a"/>
        <stop offset="1" stop-color="#3a0406"/>
      </linearGradient>
    </defs>
    <rect x="167" y="37" width="865" height="8" fill="url(#damage-line)"/>
    <circle cx="167" cy="41" r="20" fill="#fff" stroke="#d85a5c" stroke-width="5"/>
    <circle cx="353" cy="41" r="33" fill="#c8383c" stroke="#d9585b" stroke-width="6"/>
    <circle cx="539" cy="41" r="23" fill="#a01f25" stroke="#b5373b" stroke-width="5"/>
    <circle cx="705" cy="41" r="23" fill="#7d1217" stroke="#8f2328" stroke-width="5"/>
    <circle cx="867" cy="41" r="23" fill="#5f0b0f" stroke="#731a1e" stroke-width="5"/>
    <circle cx="1032" cy="41" r="24" fill="#2e0305" stroke="#4a0c0f" stroke-width="5"/>
  </svg>
  <div class="abs damage-label" style="left:82px;top:1820px">Lost<br>Income</div>
  <div class="abs damage-label" style="left:268px;top:1820px">Hospital &amp; medical<br>expenses</div>
  <div class="abs damage-label" style="left:454px;top:1820px">Pain &amp;<br>suffering</div>
  <div class="abs damage-label" style="left:620px;top:1820px">Diminished earning<br>capacity</div>
  <div class="abs damage-label" style="left:782px;top:1820px">Emotional<br>distress</div>
  <div class="abs damage-label" style="left:947px;top:1820px">Impaired<br>enjoyment</div>
</section>

<section>
  <h2 class="abs section-title" style="left:0;top:1972px;width:1200px;text-align:center;font-size:25px">CLIENT TESTIMONIALS</h2>
  <div class="abs" style="left:540px;top:2020px;width:120px;height:2px;background:var(--maroon)"></div>

  <div class="abs testi-photo" style="left:100px;top:2066px"><span role="img" aria-label="Photo of a client in a suit and glasses"></span></div>
  <div class="abs quote-mark" style="left:273px;top:2080px">&ldquo;</div>
  <div class="abs testi-name" style="left:275px;top:2120px">Nostrum Exercitatio</div>
  <div class="abs testi-role" style="left:275px;top:2155px">Manager</div>
  <p class="abs testi-text" style="left:99px;top:2211px">Quis autem vel eum iure reprehenderit qui in ea voluptate velit esse quam nihil molestiae consequatur, vel illum qui dolorem eum fugiat.</p>

  <div class="abs testi-photo" style="left:631px;top:2066px"><span role="img" aria-label="Photo of a smiling client in a suit"></span></div>
  <div class="abs quote-mark" style="left:803px;top:2080px">&ldquo;</div>
  <div class="abs testi-name" style="left:805px;top:2120px">Eiusmod Reprehen</div>
  <div class="abs testi-role" style="left:805px;top:2155px">Team Leader</div>
  <p class="abs testi-text" style="left:629px;top:2211px">Quis autem vel eum iure reprehenderit qui in ea voluptate velit esse quam nihil molestiae consequatur, vel illum qui dolorem eum fugiat.</p>
</section>

<footer>
  <div class="abs footer" role="img" aria-label="Red-toned background photo of people in an office"></div>
  <h2 class="abs footer-title">Contact Us</h2>
  <div class="abs footer-rule"></div>

  <div class="abs f-icon" style="left:99px;top:2446px">
    <svg width="18" height="13" viewBox="0 0 18 13"><rect width="18" height="13" rx="1.5" fill="#9b2a2e"/><path d="M1 1l8 6 8-6" fill="none" stroke="#fff" stroke-width="1.4"/></svg>
  </div>
  <div class="abs f-text" style="left:169px;top:2455px">info@vantholmlegal.example</div>

  <div class="abs f-icon" style="left:99px;top:2528px">
    <svg width="16" height="22" viewBox="0 0 16 22"><path d="M8 1a7 7 0 00-7 7c0 5 7 13 7 13s7-8 7-13a7 7 0 00-7-7z" fill="none" stroke="#9b2a2e" stroke-width="1.8"/><circle cx="8" cy="8" r="2.5" fill="#9b2a2e"/></svg>
  </div>
  <div class="abs f-text" style="left:169px;top:2522px">2200 Larkspur Ave #410<br>Harbor City, PA, 19000</div>

  <div class="abs f-icon" style="left:99px;top:2602px">
    <svg width="20" height="20" viewBox="0 0 24 24"><path d="M6.6 10.8a15.1 15.1 0 006.6 6.6l2.2-2.2a1 1 0 011-.25 11.4 11.4 0 003.6.6 1 1 0 011 1V20a1 1 0 01-1 1A17 17 0 013 4a1 1 0 011-1h3.5a1 1 0 011 1 11.4 11.4 0 00.6 3.6 1 1 0 01-.25 1z" fill="none" stroke="#9b2a2e" stroke-width="1.8"/></svg>
  </div>
  <div class="abs f-text" style="left:169px;top:2611px">Mobile: (555) 014-2290</div>

  <div class="abs f-lead">If you prefer, please provide your contact information below,</div>
  <div class="abs f-field" style="left:484px;top:2414px;width:290px;height:39px">Your Name</div>
  <div class="abs f-field" style="left:809px;top:2414px;width:290px;height:39px">Your Company</div>
  <div class="abs f-field" style="left:484px;top:2468px;width:290px;height:39px">Your Email</div>
  <div class="abs f-field" style="left:809px;top:2468px;width:290px;height:39px">Phone</div>
  <div class="abs f-field" style="left:484px;top:2522px;width:615px;height:88px;align-items:flex-start;padding-top:8px">Comments</div>
  <div class="abs btn send-btn">SEND NOW</div>

  <div class="abs footer-divider"></div>
  <div class="abs copyright">Copyright © 2016 Vantholm Injury Law Group. All rights reserved</div>
  <div class="abs f-social" style="left:948px"></div>
  <div class="abs f-social" style="left:990px"></div>
  <div class="abs f-social" style="left:1032px"></div>
  <div class="abs f-social" style="left:1074px"></div>
</footer>

</body>
</html>
```